UL Aesthetic improvement on full website

brightmeadowhq.com
We need someone to improve the current website brightmeadowhq.com
Some designed to fail to follow isntruction and deliver. please find attached summary latest design requirement, please follow and read each of the requirements carefully and submit max two versions only. The winner would have to deliver within 5 days

Sample reference : velorix.net/html/bluepark/#
(previous winner cant deliver)
*All of our wording and graphic content are updated, designer wouldn't involve in recreating any content.
Designer may use template or own material. delivery in html and implement on our WordPress server

please submit about us the project submission.
upon the winning, you have to maintain sub content / pages and submit the full site with your improved version of full websites including inner pages

Low design quality

Target Market(s)

general audience

Industry/Entity Type

social service

Number of Pages Required

5+ page

Requirements
Must have
• feeling and look similar to quindo dot com
Nice to have
• extend the same style to other pages

```html
<!DOCTYPE html>
<html lang="en">
<head>
<meta charset="utf-8">
<title>Bright Meadow – New Way of Giving</title>
<link href="https://fonts.googleapis.com/css2?family=Poppins:wght@300;400;500;600&display=swap" rel="stylesheet">
<style>
:root{
  --coral:#f26b6b;
  --coral-soft:#f78f8a;
  --blush:#fde4e3;
  --lavender:#dfe3fb;
  --ink:#2f2f33;
  --body:#5d5d63;
  --muted:#9a9aa0;
  --line:#ececee;
  --white:#ffffff;
}
*{box-sizing:border-box;margin:0;padding:0}
html,body{width:1200px;height:3832px;overflow:hidden}
body{font-family:'Poppins',sans-serif;color:var(--ink);background:var(--white);position:relative}
.abs{position:absolute}
.bg-layer{position:absolute;left:0;width:1200px}
.eyebrow{font-size:11px;font-weight:500;letter-spacing:.5px;color:var(--coral);text-transform:uppercase}
.btn{position:absolute;display:flex;align-items:center;justify-content:center;background:var(--coral);color:var(--white);font-size:13px;font-weight:500;border-radius:22px}
.para{font-size:12.5px;line-height:21px;color:var(--body);font-weight:300}
.section-title{font-size:33px;font-weight:500;color:var(--ink)}
.center{left:0;width:1200px;text-align:center}

/* brand */
.brand{display:flex;align-items:center;gap:7px;font-weight:600;color:var(--ink);white-space:nowrap}
.brand-dot{border-radius:50%;background:var(--coral);flex:none}

/* nav */
.nav-link{top:34px;font-size:12px;font-weight:500;color:var(--ink)}
.nav-link.active{color:var(--coral);border-bottom:1px solid var(--coral);padding-bottom:2px}
.login{left:995px;top:24px;width:117px;height:36px;font-size:13px}

/* hero */
.welcome-card{left:88px;top:192px;width:495px;height:192px;background:var(--white);box-shadow:0 8px 30px rgba(242,107,107,.08)}
.welcome-card .eyebrow{position:absolute;left:32px;top:30px}
.hero-title{position:absolute;left:32px;top:50px;font-size:32px;line-height:39px;font-weight:500}
.hero-title span{color:var(--coral)}
.goals{position:absolute;left:32px;top:139px;font-size:12px;font-weight:600;color:#2a6fb5}
.phone{border-radius:26px;background:linear-gradient(160deg,#fff6f4,#fde0dc);border:7px solid #2b2b2e;box-shadow:0 10px 25px rgba(0,0,0,.15)}

/* video */
.video{left:88px;top:654px;width:455px;height:305px;background:linear-gradient(180deg,#ffffff 0%,#e8eefc 45%,#c9d5f6 88%,#d8d8dc 100%);box-shadow:0 6px 20px rgba(0,0,0,.12)}
.play{left:286px;top:778px;width:60px;height:60px;border-radius:50%;background:var(--white);box-shadow:0 4px 14px rgba(0,0,0,.15);display:flex;align-items:center;justify-content:center}

/* cards */
.card{top:1866px;width:232px;height:399px;background:#fff3f2}
.card .thumb{height:198px}
.card h3{position:absolute;left:24px;top:226px;width:190px;font-size:14px;line-height:19px;font-weight:500;color:var(--ink)}
.card p{position:absolute;left:24px;top:276px;width:180px;font-size:12px;line-height:19px;color:var(--body);font-weight:300}
.card a{position:absolute;left:24px;top:367px;font-size:12px;font-weight:500;color:var(--coral);text-decoration:none}

.partner{width:90px;height:26px;border-radius:4px;background:#eef0f6}
.insta{top:3001px;width:156px;height:155px}

/* newsletter */
.field{top:3317px;height:42px;border-radius:21px;background:var(--white);font-size:12px;color:var(--muted);padding-left:24px;display:flex;align-items:center}

/* footer */
.foot-head{font-size:19px;font-weight:500;color:var(--coral)}
.foot-list{list-style:none;font-size:12.5px;line-height:25px;color:var(--body)}
.social{top:3685px;width:38px;height:38px;border-radius:50%;background:var(--coral)}
</style>
</head>
<body>

<!-- background bands -->
<svg class="bg-layer" style="top:0;height:540px" viewBox="0 0 1200 540" preserveAspectRatio="none" aria-hidden="true">
  <defs><linearGradient id="heroG" x1="0" y1="0" x2="0" y2="1"><stop offset="0" stop-color="#fde3e1"/><stop offset="1" stop-color="#fdeceb"/></linearGradient></defs>
  <path d="M0 0H1200V470C1000 430 850 520 600 500C380 480 200 440 0 500Z" fill="url(#heroG)"/>
</svg>
<svg class="bg-layer" style="top:1040px;height:680px" viewBox="0 0 1200 680" preserveAspectRatio="none" aria-hidden="true">
  <path d="M0 50C200 100 400 90 600 40C800 -5 1000 0 1200 40V610C1000 640 800 570 600 590C380 612 200 650 0 620Z" fill="var(--lavender)"/>
</svg>
<svg class="bg-layer" style="top:1660px;height:790px" viewBox="0 0 1200 790" preserveAspectRatio="none" aria-hidden="true">
  <defs><linearGradient id="insG" x1="0" y1="0" x2="0" y2="1"><stop offset="0" stop-color="#fff1f0"/><stop offset=".6" stop-color="#fde1df"/><stop offset="1" stop-color="#fbcbc8"/></linearGradient></defs>
  <path d="M0 40C300 70 700 0 1200 30V700C950 720 800 760 600 740C380 716 200 790 0 760Z" fill="url(#insG)"/>
</svg>
<svg class="bg-layer" style="top:2770px;height:200px" viewBox="0 0 1200 200" preserveAspectRatio="none" aria-hidden="true">
  <path d="M0 20C300 80 800 -20 1200 40V200H0Z" fill="#fff4f3"/>
</svg>
<svg class="bg-layer" style="top:2970px;height:280px" viewBox="0 0 1200 280" preserveAspectRatio="none" aria-hidden="true">
  <rect width="1200" height="280" fill="#fff4f3"/>
</svg>
<svg class="bg-layer" style="top:3230px;height:300px" viewBox="0 0 1200 300" preserveAspectRatio="none" aria-hidden="true">
  <path d="M0 0H1200V0C900 0 700 40 0 30Z" fill="#fff4f3"/>
  <path d="M0 30C400 60 800 -10 1200 25V270C900 300 600 250 300 270C180 278 80 295 0 280Z" fill="var(--coral-soft)"/>
</svg>

<!-- nav -->
<div class="abs brand" style="left:89px;top:31px;font-size:15px"><span class="brand-dot" style="width:16px;height:16px"></span>Bright Meadow</div>
<div class="abs nav-link active" style="left:445px">HOME</div>
<div class="abs nav-link" style="left:520px">ABOUT US</div>
<div class="abs nav-link" style="left:623px">OUR STORY</div>
<div class="abs nav-link" style="left:733px">SOCIAL IMPACT</div>
<div class="abs nav-link" style="left:870px">JOIN US</div>
<div class="btn login">
  <svg width="12" height="12" viewBox="0 0 12 12" style="margin-right:6px" aria-hidden="true"><circle cx="6" cy="3.5" r="2.8" fill="#fff"/><path d="M0.5 12C0.5 8 3 7 6 7S11.5 8 11.5 12Z" fill="#fff"/></svg>Login
</div>

<!-- hero -->
<div class="abs welcome-card">
  <div class="eyebrow">Welcome</div>
  <h1 class="hero-title">New Way of Giving<br><span>Social Inclusion</span></h1>
  <div class="goals">Shared Goals</div>
</div>
<div class="abs phone" style="left:638px;top:167px;width:190px;height:378px" role="img" aria-label="App screen showing featured merchants"></div>
<div class="abs phone" style="left:895px;top:167px;width:188px;height:376px" role="img" aria-label="App screen showing kindness currency and nearby area"></div>
<div class="abs phone" style="left:763px;top:110px;width:184px;height:378px" role="img" aria-label="App screen showing a merchant menu"></div>

<!-- hello -->
<div class="abs video" role="img" aria-label="Illustrated city skyline video thumbnail"></div>
<div class="abs play"><svg width="18" height="20" viewBox="0 0 18 20" aria-hidden="true"><path d="M3 1L17 10L3 19Z" fill="var(--coral)"/></svg></div>
<div class="abs eyebrow" style="left:616px;top:650px">Let's talk about something good</div>
<h2 class="abs section-title" style="left:616px;top:668px">Hello, Bright Citizens!</h2>
<p class="abs para" style="left:616px;top:730px;width:500px">Just like you, we resonate with a variety of social causes. At the core of everything, we believe that many societal challenges could be minimized merely by being more kind to one another and showing more trust in each other, especially during these difficult times.</p>
<p class="abs para" style="left:616px;top:835px;width:500px">Therefore, we digitalised the traditional concept of "Paying-it-forward" to cultivate the new normal with timely help to include everyone. We strengthens the invisible community before it's too late.</p>
<div class="btn" style="left:616px;top:923px;width:135px;height:39px">Read More</div>

<!-- brand story -->
<div class="abs" style="left:97px;top:1212px;width:416px;height:357px;border-radius:30px;background:linear-gradient(90deg,#a9c2f0,#f59ac8,#b8b8f2)" role="img" aria-label="Illustration of three people standing together"></div>
<h2 class="abs section-title" style="left:616px;top:1228px">The Brand Story</h2>
<p class="abs para" style="left:616px;top:1286px;width:496px">Back in the 1980s, my family received generous donations and small hand-written notes containing good wishes through a newspaper fund raising for my mum's medical expenses.</p>
<p class="abs para" style="left:616px;top:1369px;width:496px">I vividly remember some old and tattered notes from strangers. We ended up with double the amount that was needed, and my parents used the remaining sum to support other patients...</p>
<div class="abs" style="left:616px;top:1465px;font-size:13px;font-weight:500;color:var(--coral)">With you, I believe we can do more.</div>
<div class="abs" style="left:616px;top:1494px;width:64px;height:64px;border-radius:50%;background:linear-gradient(135deg,#e9c4b3,#8a6a5c)" role="img" aria-label="Portrait of the founder"></div>
<div class="abs" style="left:700px;top:1500px;width:125px;height:40px;background:linear-gradient(90deg,rgba(47,47,51,.15),rgba(47,47,51,.05));border-radius:6px" role="img" aria-label="Founder's signature"></div>
<div class="abs" style="left:783px;top:1543px;font-size:10px;color:var(--muted)">Founder</div>
<div class="btn" style="left:920px;top:1509px;width:151px;height:39px">Read More</div>

<!-- inspirations -->
<div class="abs eyebrow center" style="top:1774px">Updates</div>
<h2 class="abs section-title center" style="top:1792px">Inspirations</h2>
<div class="abs card" style="left:88px"><div class="thumb" style="background:linear-gradient(135deg,#3a3a44,#a77d68)" role="img" aria-label="Photo of a handshake"></div><h3>Lorem ipsum dolor sit amet, consectetur</h3><p>Sed ut perspiciatis unde omnis iste natus error sit voluptatem accusantium doloremqu.</p><a href="#">Read More</a></div>
<div class="abs card" style="left:352px"><div class="thumb" style="background:linear-gradient(135deg,#0e2c55,#1f7cc0)" role="img" aria-label="Photo of a non-profit concept with app icons"></div><h3>Lorem ipsum dolor sit amet, consectetur</h3><p>Sed ut perspiciatis unde omnis iste natus error sit voluptatem accusantium doloremqu.</p><a href="#">Read More</a></div>
<div class="abs card" style="left:616px"><div class="thumb" style="background:linear-gradient(135deg,#d9b9c9,#5c4b5a)" role="img" aria-label="Photo of hands typing on a laptop beside a non-profit sign"></div><h3>Lorem ipsum dolor sit amet, consectetur</h3><p>Sed ut perspiciatis unde omnis iste natus error sit voluptatem accusantium doloremqu.</p><a href="#">Read More</a></div>
<div class="abs card" style="left:880px"><div class="thumb" style="background:linear-gradient(135deg,#c7d3e3,#6e8bb0)" role="img" aria-label="Photo of financial charts on a desk"></div><h3>Lorem ipsum dolor sit amet, consectetur</h3><p>Sed ut perspiciatis unde omnis iste natus error sit voluptatem accusantium doloremqu.</p><a href="#">Read More</a></div>

<!-- partners -->
<div class="abs eyebrow center" style="top:2512px">Our kind partners</div>
<h2 class="abs section-title center" style="top:2530px">In <span style="color:var(--coral)">Partnership</span> With</h2>
<div class="abs partner" style="left:163px;top:2601px" role="img" aria-label="Partner badge"></div>
<div class="abs partner" style="left:319px;top:2601px" role="img" aria-label="Partner badge"></div>
<div class="abs partner" style="left:475px;top:2601px" role="img" aria-label="Partner badge"></div>
<div class="abs partner" style="left:624px;top:2601px" role="img" aria-label="Partner badge"></div>
<div class="abs partner" style="left:777px;top:2601px" role="img" aria-label="Partner badge"></div>
<div class="abs partner" style="left:929px;top:2601px" role="img" aria-label="Partner badge"></div>
<div class="abs partner" style="left:168px;top:2659px" role="img" aria-label="Partner badge"></div>
<div class="abs partner" style="left:318px;top:2659px" role="img" aria-label="Partner badge"></div>
<div class="abs partner" style="left:472px;top:2659px" role="img" aria-label="Partner badge"></div>
<div class="abs partner" style="left:627px;top:2659px" role="img" aria-label="Partner badge"></div>
<div class="abs partner" style="left:777px;top:2659px" role="img" aria-label="Partner badge"></div>

<!-- follow -->
<div class="abs eyebrow center" style="top:2902px">Follow</div>
<h2 class="abs section-title center" style="top:2920px">@brightmeadowsg</h2>
<div class="abs insta" style="left:88px;background:linear-gradient(180deg,#cfe4e6,#6f9a8a)" role="img" aria-label="Illustration of recycling bins on a street"></div>
<div class="abs insta" style="left:262px;background:linear-gradient(135deg,#c8161b,#6b1a16)" role="img" aria-label="Photo of hands painted red forming a heart"></div>
<div class="abs insta" style="left:434px;background:linear-gradient(135deg,#d8dbe0,#6d7079)" role="img" aria-label="Photo of a video call on a laptop"></div>
<div class="abs insta" style="left:608px;background:linear-gradient(180deg,#cfe4e6,#6f9a8a)" role="img" aria-label="Illustration of recycling bins on a street"></div>
<div class="abs insta" style="left:782px;background:linear-gradient(135deg,#c8161b,#6b1a16)" role="img" aria-label="Photo of hands painted red forming a heart"></div>
<div class="abs insta" style="left:955px;background:linear-gradient(135deg,#d8dbe0,#6d7079)" role="img" aria-label="Photo of a video call on a laptop"></div>

<!-- newsletter -->
<h2 class="abs" style="left:89px;top:3333px;font-size:25px;font-weight:500;color:var(--ink)">Subscribe to Our Newsletter</h2>
<p class="abs" style="left:89px;top:3378px;width:460px;font-size:13px;line-height:21px;font-weight:500;color:var(--ink)">Let's stay in touch! We would like to keep you inspired with our Kindness stories and community events.</p>
<div class="abs field" style="left:630px;width:232px">First Name</div>
<div class="abs field" style="left:879px;width:233px">Email</div>
<div class="abs" style="left:643px;top:3376px;width:18px;height:18px;border-radius:3px;background:var(--white)"></div>
<div class="abs" style="left:670px;top:3376px;font-size:12px;color:var(--ink)">By continuing, you accept the privacy policy</div>
<div class="btn" style="left:630px;top:3416px;width:160px;height:37px;background:#ef5757">Subscribe</div>

<!-- footer -->
<div class="abs brand" style="left:89px;top:3602px;font-size:11px;gap:5px"><span class="brand-dot" style="width:11px;height:11px"></span>Bright Meadow</div>
<div class="abs foot-head" style="left:184px;top:3572px">Follow us and stay updated!</div>
<p class="abs" style="left:184px;top:3610px;font-size:12.5px;line-height:19px;color:var(--body)">A Singapore Social Enterprise.<br>In a world where you can be anything, be kind.</p>
<div class="abs social" style="left:186px" role="img" aria-label="Social link"></div>
<div class="abs social" style="left:235px" role="img" aria-label="Social link"></div>
<div class="abs social" style="left:284px" role="img" aria-label="Social link"></div>
<div class="abs social" style="left:333px" role="img" aria-label="Social link"></div>
<div class="abs foot-head" style="left:688px;top:3573px">Quick Link</div>
<ul class="abs foot-list" style="left:689px;top:3604px">
  <li style="text-decoration:underline">Home</li><li>About Us</li><li>Our Story</li><li>Social Impact</li><li>Bright Meadow</li>
</ul>
<div class="abs foot-head" style="left:926px;top:3573px">Links</div>
<ul class="abs foot-list" style="left:927px;top:3604px">
  <li>Meadow Business</li><li>Merchant</li><li>The Meadow Gift</li><li>FAQs</li><li>Contact Us</li>
</ul>
<div class="abs" style="left:88px;top:3773px;width:1024px;height:1px;background:var(--line)"></div>
<div class="abs center" style="top:3792px;font-size:11px;color:var(--body)">COPYRIGHT © 2021 BRIGHT MEADOW SINGAPORE</div>

</body>
</html>
```